We are looking for an effective ad to recruit work from home Loan Officers for our Mortgage Brokerage.
Use the following text...
Earn Mortgage Income in your sleep. Its as easy as 1, 2, 3.....
1) Solicit Potential Applicants (Word of Mouth, Email, Social Media etc.)
2) Take Complete Applications & Submit Them
3) Wait to Get Paid.......(Avg. $2,500 per closing)
"You open the door, we'll finish the deal"
No Experience Necessary
No Goals or Quotas
No Office Hours / Work from Home Office
...and We Fully Reimburse ALL LICENSING FEES!!
Email Resume to mwelby@brightharborloans.example
Bright Harbor Lending Group, Inc.
947 W Caldwell Avenue, #318
Baltimore, MD 21230
NMLS #731860
www.brightharborloans.example
Phone (800) 555-0142
Licensed Mortgage Broker in MD and DC since 1997
Target Market(s)
Professionals looking to earn part time income at Loan Officers, preferably with strong social media following.
Industry/Entity Type
Loan
Look and feel

```html
<!DOCTYPE html>
<html lang="en">
<head>
<meta charset="utf-8">
<title>Bright Harbor Lending Group – Loan Officers Wanted</title>
<link rel="stylesheet" href="https://fonts.googleapis.com/css2?family=Arvo:ital,wght@0,700;1,400;1,700&family=Questrial&family=Arimo:wght@400&family=Abel&family=Montserrat:wght@700;800&display=swap">
<style>
  :root {
    --blue: #0b5ea9;
    --blue-light: #2a79ba;
    --teal-blue: #1f6896;
    --olive: #a99429;
    --tan: #dcd097;
    --cream: #ebe6cb;
    --white: #ffffff;
  }
  * { margin: 0; padding: 0; box-sizing: border-box; }
  html, body { width: 928px; height: 1200px; overflow: hidden; background: var(--white); }
  .ad { position: relative; width: 928px; height: 1200px; overflow: hidden; background: var(--white); }

  .headline {
    position: absolute; left: 20px; top: 30px; width: 305px;
    font-family: "Arvo", serif; font-weight: 700; font-style: italic;
    font-size: 53px; line-height: 63px; color: var(--blue); text-align: center;
    white-space: nowrap;
  }

  .step { position: absolute; font-family: "Arimo", sans-serif; font-weight: 400; letter-spacing: -1px; }
  .step-num { font-family: "Arvo", serif; font-weight: 700; letter-spacing: 0; }

  .step-1 {
    left: 325px; top: 44px; width: 308px; height: 303px;
    background: var(--blue); color: var(--white);
    border-radius: 50% 50% 0 50%;
  }
  .step-1 .step-num { position: absolute; left: 88px; top: 26px; font-size: 96px; line-height: 1; }
  .step-1 .step-title { position: absolute; left: 0; top: 56px; width: 256px; font-size: 44px; line-height: 51px; text-align: right; }
  .step-1 .step-title span { display: block; }
  .step-1 .step-note { position: absolute; left: 30px; top: 220px; width: 265px; font-size: 22px; line-height: 36px; text-align: center; letter-spacing: -0.5px; }

  .step-2 {
    left: 650px; top: 81px; width: 268px; height: 266px;
    background: var(--tan); color: var(--blue);
    border-radius: 50% 50% 50% 0;
  }
  .step-2 .step-num { position: absolute; left: 24px; top: 44px; font-size: 86px; line-height: 1; }
  .step-2 .take { position: absolute; left: 90px; top: 52px; font-size: 44px; line-height: 1; }
  .step-2 .complete { position: absolute; left: 93px; top: 103px; font-size: 30px; line-height: 1; }
  .step-2 .rest { position: absolute; left: 0; top: 142px; width: 228px; font-size: 37px; line-height: 42px; text-align: center; }

  .easy-band {
    position: absolute; left: 0; top: 367px; width: 637px; height: 107px;
    background: var(--olive); color: var(--white);
    font-family: "Questrial", sans-serif; font-size: 57px; line-height: 107px;
    padding-left: 56px; white-space: nowrap;
  }

  .step-3 {
    left: 650px; top: 367px; width: 210px; height: 211px;
    background: var(--blue-light); color: var(--white);
    border-radius: 0 50% 50% 50%;
  }
  .step-3 .step-num { position: absolute; left: 14px; top: 14px; font-size: 80px; line-height: 1; color: var(--tan); }
  .step-3 .wait { position: absolute; left: 72px; top: 30px; font-size: 45px; line-height: 1; }
  .step-3 .rest { position: absolute; left: 0; top: 78px; width: 210px; font-size: 45px; line-height: 50px; text-align: center; }

  .avg {
    position: absolute; left: 100px; top: 495px; width: 480px; text-align: center;
    font-family: "Arimo", sans-serif; font-size: 36px; letter-spacing: -0.5px; color: var(--blue); white-space: nowrap;
  }

  .tagline {
    position: absolute; left: 0; top: 588px; width: 928px; text-align: center;
    font-family: "Questrial", sans-serif; font-size: 41px; color: var(--olive); white-space: nowrap;
  }

  .perks-band {
    position: absolute; left: 0; top: 658px; width: 928px; height: 214px;
    background: linear-gradient(90deg, var(--cream) 0%, var(--cream) 25%, var(--white) 60%);
  }
  .perks {
    position: absolute; left: 48px; top: 35px; list-style: none;
    font-family: "Arvo", serif; font-style: italic; font-weight: 400;
    font-size: 33px; line-height: 36px; color: var(--teal-blue); white-space: nowrap;
  }
  .perks li::before { content: "\2022\00a0"; }
  .perks li.cont::before { content: ""; }

  .brand-mark {
    position: absolute; left: 520px; top: 40px; width: 370px; height: 140px;
    display: flex; align-items: center; gap: 16px;
    font-family: "Questrial", sans-serif; font-size: 30px; line-height: 36px; color: var(--blue);
  }
  .brand-mark .dot { flex: 0 0 58px; height: 58px; border-radius: 50%; background: var(--tan); }

  .reimburse {
    position: absolute; left: 0; top: 885px; width: 928px; text-align: center;
    font-family: "Arvo", serif; font-weight: 700; font-size: 33px; color: var(--olive); white-space: nowrap;
  }

  .social-badge {
    position: absolute; z-index: 2; left: 35px; top: 963px; width: 217px; height: 71px;
    background: var(--white); border: 3px solid var(--blue); border-radius: 4px;
    display: flex; align-items: center; gap: 10px; padding-left: 14px;
    font-family: "Questrial", sans-serif; font-size: 19px; line-height: 22px; color: var(--blue);
  }
  .social-badge .sq { flex: 0 0 32px; height: 32px; background: var(--blue); }

  .email {
    position: absolute; left: 272px; top: 951px; width: 640px; text-align: right;
    font-family: "Questrial", sans-serif; font-size: 25px; color: var(--blue); white-space: nowrap;
  }

  .url-band {
    position: absolute; left: 0; top: 1000px; width: 928px; height: 43px;
    background: var(--olive);
  }
  .url {
    position: absolute; left: 262px; top: 990px; width: 650px; text-align: center;
    font-family: "Montserrat", sans-serif; font-weight: 800; font-size: 35px; line-height: 60px;
    color: var(--white); white-space: nowrap;
  }

  .footer {
    position: absolute; left: 0; top: 1043px; width: 928px; height: 157px;
    background: var(--blue); color: var(--white);
    font-family: "Abel", sans-serif; font-size: 30px; line-height: 44px; text-align: center;
    padding-top: 6px; white-space: nowrap;
  }
  .footer .phone { font-family: "Montserrat", sans-serif; font-weight: 700; font-size: 37px; }
</style>
</head>
<body>
<main class="ad">
  <h1 class="headline">Earn<br>Mortgage<br>Income<br>in your<br>sleep.</h1>

  <section class="step step-1">
    <span class="step-num">1</span>
    <p class="step-title"><span>Solicit</span><span>Potential</span><span>Applicants</span></p>
    <p class="step-note">(Word of Mouth, Email,<br>Social Media etc.)</p>
  </section>

  <section class="step step-2">
    <span class="step-num">2</span>
    <span class="take">Take</span>
    <span class="complete">Complete</span>
    <p class="rest">Applications<br>&amp; Submit<br>Them</p>
  </section>

  <div class="easy-band">Its as easy as 1, 2, 3...</div>

  <section class="step step-3">
    <span class="step-num">3</span>
    <span class="wait">Wait</span>
    <p class="rest">to Get<br>Paid</p>
  </section>

  <p class="avg">(Avg. $2,500 per closing)</p>

  <p class="tagline">"You open the door, we'll finish the deal"</p>

  <section class="perks-band">
    <ul class="perks">
      <li>No Experience Necessary</li>
      <li>No Goals or Quotas</li>
      <li>No Office Hours</li>
      <li class="cont">/ Work from Home Office</li>
    </ul>
    <div class="brand-mark"><span class="dot"></span><span>Bright Harbor Lending Group, Inc.</span></div>
  </section>

  <p class="reimburse">...and We Fully Reimburse ALL LICENSING FEES!!</p>

  <p class="email">Email Resume to mwelby@brightharborloans.example</p>

  <div class="url-band"></div>
  <p class="url">www.brightharborloans.example</p>

  <div class="social-badge"><span class="sq"></span><span>Like us on<br>FriendSpace</span></div>

  <footer class="footer">
    <div>Bright Harbor Lending Group, Inc. 947 W Caldwell Avenue, #318 Baltimore,</div>
    <div>MD 21230 NMLS #731860 &nbsp;<span class="phone">Phone (800) 555-0142</span></div>
    <div>Licensed Mortgage Broker in MD and DC since 1997</div>
  </footer>
</main>
</body>
</html>
```